Need a Brochure Design

We need a brochure designed (A4 two sides or A3 foldable which is equal to 2 x A4 = total of four pages )

Brief and Logo attached.

```html
<!DOCTYPE html>
<html lang="en">
<head>
<meta charset="utf-8">
<title>Nest Styling Co – Brochure</title>
<link href="https://fonts.googleapis.com/css2?family=Lato:wght@400;700;900&display=swap" rel="stylesheet">
<style>
  :root {
    --orange: #e57f3d;
    --ink: #1f1f1f;
    --text: #3a3a3a;
    --paper: #f7f7f7;
    --peach: #f1dccb;
    --band-light: #e2e2e2;
    --band-mid: #8e8e8e;
    --band-dark: #6e6a6a;
  }
  * { box-sizing: border-box; margin: 0; padding: 0; }
  html, body { width: 1200px; height: 2668px; overflow: hidden; }
  body { font-family: "Lato", Arial, sans-serif; color: var(--text); }

  .band { position: absolute; left: 0; width: 1200px; }
  .band--covers { top: 0; height: 930px; background: var(--band-light); }
  .band--spread { top: 930px; height: 870px; background: var(--band-mid); }
  .band--inside { top: 1800px; height: 868px; background: var(--band-dark); }

  .page {
    position: absolute; background: var(--paper); overflow: hidden;
    box-shadow: 0 6px 18px rgba(0,0,0,.18);
  }

  /* Front cover component, sized by font-size */
  .cover { width: 36em; height: 50.9em; }
  .cover__strip { position: absolute; left: 66%; top: 26%; right: 0; bottom: 0; background: var(--orange); }
  .cover__block { position: absolute; left: 60%; top: 84%; right: 0; bottom: 0; background: var(--orange); }
  .cover__photo {
    position: absolute; left: 0; top: 17%; width: 80%; height: 49%;
    border: .4em solid #fff; border-left: 0;
    background: linear-gradient(160deg, #eceae6 0%, #d9d6d0 40%, #a9a39a 70%, #8c8578 100%);
  }
  .cover__headline {
    position: absolute; left: 7%; top: 70.5%; white-space: nowrap;
    font-weight: 900; font-size: 1.9em; line-height: 1.02; color: var(--ink); text-transform: uppercase;
  }
  .cover__headline .accent { color: var(--orange); }
  .cover__url { position: absolute; left: 7%; top: 87%; font-weight: 700; font-size: 1.05em; color: var(--ink); white-space: nowrap; }

  .brand { position: absolute; display: flex; align-items: center; gap: .5em; }
  .brand__dot { width: 1.6em; height: 1.6em; border-radius: 50%; background: var(--peach); }
  .brand__name { font-weight: 700; font-size: .95em; letter-spacing: .12em; color: var(--text); text-transform: uppercase; white-space: nowrap; }
  .cover .brand { top: 5%; right: 7%; }

  .cover--single { font-size: 15.4px; left: 323px; top: 75px; }
  .cover--spread { font-size: 12.2px; left: 600px; top: 128px; box-shadow: none; }

  /* Back cover */
  .back { left: 161px; top: 128px; width: 439px; height: 621px; box-shadow: none; font-size: 12.2px; }
  .spread-shell { position: absolute; left: 161px; top: 128px; width: 878px; height: 621px; box-shadow: 0 6px 18px rgba(0,0,0,.22); }
  .back .brand { left: 7%; bottom: 19%; }
  .contact { position: absolute; left: 7%; bottom: 6%; font-size: 10px; line-height: 1.55; color: var(--ink); }
  .contact__row { display: flex; align-items: center; gap: 6px; }
  .contact__row svg { width: 10px; height: 10px; fill: var(--orange); }

  /* Inside spread */
  .inside { left: 128px; top: 105px; width: 882px; height: 640px; box-shadow: 0 8px 22px rgba(0,0,0,.3); }
  .inside__text { position: absolute; left: 0; top: 0; width: 441px; height: 100%; padding: 42px 36px 0 36px; font-size: 8.6px; line-height: 1.35; color: var(--ink); }
  .inside__text p { margin-bottom: 9px; }
  .inside__photo {
    position: absolute; left: 441px; top: 0; width: 441px; height: 100%;
    background: linear-gradient(180deg, #ebe8e4 0%, #dedad4 40%, #b7aea3 70%, #d8d3cc 100%);
  }
  .section-title {
    display: block; margin: 18px 0 9px; white-space: nowrap;
    font-size: 15px; font-weight: 400; text-transform: uppercase; color: var(--ink); letter-spacing: .01em;
  }
  .section-title::before { content: ""; display: inline-block; vertical-align: -2px; width: 3px; height: 16px; margin-right: 8px; background: var(--orange); }
  .section-title .accent { color: var(--orange); }
  .checklist { list-style: none; }
  .checklist li { display: flex; align-items: center; gap: 9px; font-size: 10px; margin-bottom: 12px; }
  .checklist svg { width: 11px; height: 11px; flex: none; }
  .inside__footer { position: absolute; left: 36px; right: 36px; bottom: 28px; display: flex; align-items: center; gap: 10px; font-size: 8px; font-weight: 700; color: var(--ink); }
  .inside__footer .brand { position: static; font-size: 10px; }
  .inside__footer .rule { flex: 1; height: 1px; background: var(--ink); }
</style>
</head>
<body>

<section class="band band--covers">
  <div class="page cover cover--single">
    <div class="cover__strip"></div>
    <div class="cover__block"></div>
    <div class="cover__photo" role="img" aria-label="Photo of a bright staged living room with grey sofa, timber coffee table and black-framed window"></div>
    <div class="brand"><span class="brand__dot"></span><span class="brand__name">Nest Styling Co</span></div>
    <h1 class="cover__headline">We will give<br>your property<br><span class="accent">the best look !</span></h1>
    <div class="cover__url">www.neststylingco.com.au</div>
  </div>
</section>

<section class="band band--spread">
  <div class="spread-shell"></div>
  <div class="page back">
    <div class="brand"><span class="brand__dot"></span><span class="brand__name">Nest Styling Co</span></div>
    <div class="contact">
      <div class="contact__row"><svg viewBox="0 0 10 10"><path d="M2 0.5l2 2-1 1.2c.6 1.3 1.6 2.3 2.9 2.9l1.2-1 2 2-1.3 1.9C4 9.3.7 6 .1 1.8z"/></svg>Phone: 0400 000 123</div>
      <div class="contact__row"><svg viewBox="0 0 10 10"><path d="M5 0a3.5 3.5 0 0 1 3.5 3.5C8.5 6 5 10 5 10S1.5 6 1.5 3.5A3.5 3.5 0 0 1 5 0zm0 2.2a1.3 1.3 0 1 0 0 2.6 1.3 1.3 0 0 0 0-2.6z"/></svg>14 Elmwood Lane, Greenvale, VIC 3000</div>
      <div class="contact__row"><svg viewBox="0 0 10 10"><path d="M0 2h10v6H0zM.6 2.4 5 5.6l4.4-3.2"/></svg>Email: hello@neststylingco.com.au</div>
      <div class="contact__row"><svg viewBox="0 0 10 10"><circle cx="5" cy="5" r="4.5"/></svg>www.neststylingco.com.au</div>
    </div>
  </div>
  <div class="page cover cover--spread">
    <div class="cover__strip"></div>
    <div class="cover__block"></div>
    <div class="cover__photo" role="img" aria-label="Photo of a bright staged living room with grey sofa, timber coffee table and black-framed window"></div>
    <div class="brand"><span class="brand__dot"></span><span class="brand__name">Nest Styling Co</span></div>
    <h1 class="cover__headline">We will give<br>your property<br><span class="accent">the best look !</span></h1>
    <div class="cover__url">www.neststylingco.com.au</div>
  </div>
</section>

<section class="band band--inside">
  <div class="page inside">
    <div class="inside__text">
      <p>Hey there,</p>
      <p>I'm Mara, Owner and Creative Director of Nest Styling Co. Please let me introduce you to our amazingly creative property styling team!</p>
      <p>We are a friendly bunch who are passionate about home staging. We've been property staging apartments, townhouses, and standalone homes since 2009. An all-female powerhouse, we combine our experience in art, interior design, retail, and business to offer professional home styling throughout Melbourne.</p>

      <h2 class="section-title">Because first <span class="accent">impressions count</span></h2>
      <p>A gorgeous looking home sells faster and fetches a higher price.</p>
      <p>At Nest Styling Co, we help our property clients create a lasting impression with minimal spend. Our property vendors are usually looking for home-staging on a tight budget. They come to us searching for creative transformations to help them sell well. Thoughtfully positioned furniture and on-trend interior décor can make all the difference!</p>
      <p>Our property styling service includes a free consultation, longer rental periods, and installation and removal.</p>

      <h2 class="section-title">We're well-<span class="accent">connected</span></h2>
      <p>We have a steady flow of clients who have not yet secured their Real Estate Agents, so we'd be happy to share the love. We believe in last relationships, and we work with reputable agents across Melbourne.</p>

      <h2 class="section-title">Why choose <span class="accent">Nest Styling Co?</span></h2>
      <ul class="checklist">
        <li><svg viewBox="0 0 12 12"><circle cx="6" cy="6" r="5.2" fill="none" stroke="#e57f3d" stroke-width="1"/><path d="M3.4 6.2l1.8 1.8 3.6-3.8" fill="none" stroke="#e57f3d" stroke-width="1.2"/></svg>Experienced, enthusiastic property stylists</li>
        <li><svg viewBox="0 0 12 12"><circle cx="6" cy="6" r="5.2" fill="none" stroke="#e57f3d" stroke-width="1"/><path d="M3.4 6.2l1.8 1.8 3.6-3.8" fill="none" stroke="#e57f3d" stroke-width="1.2"/></svg>Work with low client budgets</li>
        <li><svg viewBox="0 0 12 12"><circle cx="6" cy="6" r="5.2" fill="none" stroke="#e57f3d" stroke-width="1"/><path d="M3.4 6.2l1.8 1.8 3.6-3.8" fill="none" stroke="#e57f3d" stroke-width="1.2"/></svg>Fast turnaround to a tight deadline</li>
        <li><svg viewBox="0 0 12 12"><circle cx="6" cy="6" r="5.2" fill="none" stroke="#e57f3d" stroke-width="1"/><path d="M3.4 6.2l1.8 1.8 3.6-3.8" fill="none" stroke="#e57f3d" stroke-width="1.2"/></svg>Flexible rental terms (4/6/8 weeks)</li>
        <li><svg viewBox="0 0 12 12"><circle cx="6" cy="6" r="5.2" fill="none" stroke="#e57f3d" stroke-width="1"/><path d="M3.4 6.2l1.8 1.8 3.6-3.8" fill="none" stroke="#e57f3d" stroke-width="1.2"/></svg>Happy to recommend potential customers</li>
      </ul>

      <div class="inside__footer">
        <div class="brand"><span class="brand__dot"></span><span class="brand__name">Nest Styling Co</span></div>
        <span class="rule"></span>
        <span>www.neststylingco.com.au</span>
      </div>
    </div>
    <div class="inside__photo" role="img" aria-label="Photo of a staged lounge with grey sofa, patterned rug, black coffee table, tall windows and a potted plant"></div>
  </div>
</section>

</body>
</html>
```